Letterhead for SaaS

Design a letterhead that aligns with our new business card, using our logo and color scheme and text defined in the Branding Guide to ensure consistency. Consider incorporating a subtle watermark for added elegance. The layout should reflect the card's style, creating a cohesive look across our stationery.

```html
<!DOCTYPE html>
<html lang="en">
<head>
<meta charset="UTF-8">
<title>Veltrova Letterhead</title>
<link href="https://fonts.googleapis.com/css2?family=Arimo:wght@400;700&display=swap" rel="stylesheet">
<style>
  :root {
    --paper: #f6f4f4;
    --ink: #141a26;
    --text: #4a4a4c;
    --text-soft: #5a5a5c;
    --accent: #12c0f5;
    --white: #ffffff;
    --mark-fill: #e2e0e1;
  }
  html, body {
    margin: 0;
    padding: 0;
    width: 942px;
    height: 1200px;
    overflow: hidden;
    background: var(--paper);
  }
  .letterhead {
    position: relative;
    width: 942px;
    height: 1200px;
    background: var(--paper);
    font-family: "Arimo", Arial, sans-serif;
    color: var(--text);
    overflow: hidden;
  }
  .brand {
    position: absolute;
    left: 64px;
    top: 150px;
    display: flex;
    align-items: center;
    gap: 10px;
  }
  .brand-square {
    width: 18px;
    height: 18px;
    background: var(--ink);
  }
  .brand-name {
    font-size: 26px;
    font-weight: 700;
    letter-spacing: 0.5px;
    color: var(--ink);
  }
  .watermark {
    position: absolute;
    left: 260px;
    top: 380px;
    width: 420px;
    height: 680px;
    border-radius: 50% 50% 48% 48%;
    background: radial-gradient(ellipse at center, var(--mark-fill) 0%, rgba(226,224,225,0.55) 55%, rgba(246,244,244,0) 78%);
  }
  .letter-body {
    position: absolute;
    left: 64px;
    top: 298px;
    width: 815px;
  }
  .salutation {
    font-size: 25px;
    color: var(--text-soft);
    margin: 0 0 44px;
  }
  .letter-body p.paragraph {
    font-size: 14px;
    line-height: 20px;
    margin: 0 0 20px;
    text-align: justify;
  }
  .closing {
    font-size: 14px;
    margin: 32px 0 0;
  }
  .signature {
    position: absolute;
    left: 72px;
    top: 872px;
    width: 150px;
    height: 52px;
    border-radius: 4px;
    background: linear-gradient(90deg, rgba(20,26,38,0.12), rgba(20,26,38,0.05));
  }
  .signer {
    position: absolute;
    left: 76px;
    top: 940px;
  }
  .signer-name {
    font-size: 20px;
    color: var(--text-soft);
    margin: 0 0 6px;
  }
  .signer-title {
    font-size: 15px;
    color: var(--text-soft);
    margin: 0;
  }
  .footer-band {
    position: absolute;
    left: 0;
    top: 0;
    width: 942px;
    height: 1200px;
  }
  .contact-list {
    position: absolute;
    right: 80px;
    top: 1106px;
    margin: 0;
    padding: 0;
    list-style: none;
    color: var(--white);
    font-size: 14px;
    line-height: 19px;
    text-align: right;
  }
  .contact-list li {
    display: flex;
    justify-content: flex-end;
    align-items: center;
    gap: 9px;
  }
  .contact-icon {
    width: 13px;
    height: 13px;
    flex: none;
  }
</style>
</head>
<body>
<main class="letterhead">
  <div class="watermark" role="img" aria-label="Faint brand watermark behind the letter text"></div>

  <header class="brand">
    <span class="brand-square"></span>
    <span class="brand-name">VELTROVA</span>
  </header>

  <section class="letter-body">
    <p class="salutation">Dear Mr. Parker,</p>
    <p class="paragraph">Lorem ipsum dolor sit amet, consectetur adipiscing elit. Donec orci purus, luctus vitae dignissim eu, iaculis sed purus. Vivamus faucibus, ipsum nec aliquet viverra, leo mauris condimentum ligula, sit amet sagittis enim ligula quis arcu. Nam egestas tortor id nisi porttitor mattis. In tortor ante, ultricies in suscipit a, tempus non massa. Vivamus et auctor mi. Fusce vel massa nulla. Phasellus nec eros mauris, et scelerisque orci.</p>
    <p class="paragraph">Donec malesuada orci vitae nulla accumsan porta a id massa. Quisque accumsan iaculis magna sit amet fringilla. Maecenas consequat, magna eget tincidunt semper, odio nibh rutrum mi, id feugiat ante nisi eu risus. Vestibulum nunc orci, rhoncus a placerat in, ultricies in mi. Cras mattis varius eros, vel fringilla nisi suscipit eget. Quisque scelerisque sagittis nulla at porttitor.</p>
    <p class="paragraph">Sed id augue vitae urna euismod commodo aliquet a quam. Pellentesque arcu velit, cursus et malesuada ut, consequat et diam. Nullam erat sem, rhoncus id ullamcorper vitae, rhoncus et arcu. In ultricies ultricies nulla, ut rutrum nisi iaculis at. Donec eu magna a metus ornare faucibus. Fusce aliquet faucibus ultricies. Morbi semper, est id tincidunt gravida, sem arcu adipiscing lacus, ac bibendum nulla leo eu purus. Quisque nec diam sed risus consectetur a ccumsan quis quis nibh. Vestibulum id purus lorem.</p>
    <p class="paragraph">It is a long established fact that a reader will be distracted by the readable content of a page when looking at its layout. The point of using Lorem Ipsum is that it has a more-or-less normal distribution of letters, as opposed to using 'Content here, content here', making it look like readable English. Many desktop publishing packages</p>
    <p class="closing">Sincerely,</p>
  </section>

  <div class="signature" role="img" aria-label="Handwritten signature of Daniel Harlow"></div>
  <div class="signer">
    <p class="signer-name">Daniel Harlow</p>
    <p class="signer-title">CEO/ Founder</p>
  </div>

  <svg class="footer-band" viewBox="0 0 942 1200" aria-hidden="true">
    <polygon points="296,1200 942,930 942,946 312,1200" fill="var(--accent)"/>
    <polygon points="312,1200 942,946 942,954 330,1200" fill="var(--white)"/>
    <polygon points="330,1200 942,954 942,1200" fill="var(--ink)"/>
  </svg>

  <ul class="contact-list">
    <li>(555) 014-2271
      <svg class="contact-icon" viewBox="0 0 16 16"><path d="M3.5 1.5l2.5 0 1 3.5-1.8 1.2c.8 1.8 2.2 3.2 4 4l1.2-1.8 3.5 1v2.5c0 .8-.7 1.5-1.5 1.5C6.7 13.4 2.6 9.3 2 3c0-.8.7-1.5 1.5-1.5z" fill="var(--accent)"/></svg>
    </li>
    <li>d.harlow@veltrova.com
      <svg class="contact-icon" viewBox="0 0 16 16"><rect x="1" y="3" width="14" height="10" fill="var(--accent)"/><path d="M1 3.5l7 5 7-5" fill="none" stroke="var(--ink)" stroke-width="1.3"/></svg>
    </li>
    <li>www.veltrova.com
      <svg class="contact-icon" viewBox="0 0 16 16"><circle cx="8" cy="8" r="7" fill="var(--accent)"/><path d="M1 8h14M8 1c-3 3.5-3 10.5 0 14M8 1c3 3.5 3 10.5 0 14" fill="none" stroke="var(--ink)" stroke-width="1"/></svg>
    </li>
  </ul>
</main>
</body>
</html>
```